Q-Rolls Business Card

We are a modern retail clothing store. Established in 1994. I need a presentable card that will amaze vendors when given to them.

Front: Logo in middle
Info Side:

Name: Tomas Velder
Cell: 630-812-4463
Work: 630-917-3384 EXT. 417
Email: Tomas@q-rolls-example.com
Website: www.Q-rolls-example.com

Industry/Entity Type

Business

```html
<!DOCTYPE html>
<html lang="en">
<head>
<meta charset="utf-8">
<title>Q-Rolls Business Card</title>
<link href="https://fonts.googleapis.com/css2?family=Lato:wght@400;700&display=swap" rel="stylesheet">
<style>
  :root {
    --backdrop: #e6e6e6;
    --ink: #111111;
    --paper: #ffffff;
    --swoosh: #c4c4c4;
    --text-dark: #1c1c1c;
  }
  * { margin: 0; padding: 0; box-sizing: border-box; }
  html, body { width: 1200px; height: 898px; overflow: hidden; }
  body {
    background: var(--backdrop);
    font-family: "Lato", Arial, sans-serif;
    position: relative;
  }
  .card {
    position: absolute;
    left: 300px;
    width: 600px;
    height: 343px;
    overflow: hidden;
    box-shadow: 0 3px 10px rgba(0,0,0,0.18);
  }
  .card-front { top: 60px; background: var(--ink); }
  .card-back { top: 470px; background: var(--paper); }

  .brand-name {
    font-family: "Lato", Arial, sans-serif;
    font-weight: 700;
    text-transform: uppercase;
    letter-spacing: 2px;
    white-space: nowrap;
  }
  .card-front .brand-name {
    position: absolute;
    left: 0; right: 0; top: 118px;
    text-align: center;
    font-size: 78px;
    line-height: 1;
    color: var(--paper);
  }
  .card-front .site-url {
    position: absolute;
    left: 0; right: 0; bottom: 34px;
    text-align: center;
    font-size: 14px;
    letter-spacing: 2.5px;
    color: var(--paper);
  }

  .back-shapes { position: absolute; inset: 0; }
  .card-back .brand-name {
    position: absolute;
    right: 36px; top: 42px;
    font-size: 56px;
    line-height: 1;
    color: var(--text-dark);
  }
  .holder-name {
    position: absolute;
    left: 62px; top: 198px;
    font-size: 24px;
    color: var(--text-dark);
  }
  .contact-list {
    position: absolute;
    left: 62px; top: 248px;
    list-style: none;
    font-size: 15.5px;
    color: var(--text-dark);
  }
  .contact-list li {
    display: flex;
    align-items: center;
    height: 19px;
  }
  .contact-list svg {
    width: 12px; height: 12px;
    margin-right: 14px;
    fill: var(--text-dark);
    flex: none;
  }
</style>
</head>
<body>

<section class="card card-front">
  <div class="brand-name">Q-Rolls</div>
  <div class="site-url">www.Q-rolls-example.com</div>
</section>

<section class="card card-back">
  <svg class="back-shapes" viewBox="0 0 600 343" preserveAspectRatio="none" aria-hidden="true">
    <path d="M0 0 L240 0 C150 20 60 70 0 120 Z" fill="var(--ink)"/>
    <path d="M0 120 C60 70 150 20 240 0 L262 0 C170 30 80 90 0 170 Z" fill="var(--swoosh)"/>
    <path d="M600 140 L600 343 L330 343 C450 300 540 230 600 140 Z" fill="var(--ink)"/>
    <path d="M600 80 C560 190 470 280 330 343 L300 343 C440 290 540 200 585 80 Z" fill="var(--swoosh)"/>
  </svg>

  <div class="brand-name">Q-Rolls</div>
  <div class="holder-name">Tomas Velder</div>

  <ul class="contact-list">
    <li>
      <svg viewBox="0 0 24 24"><path d="M6.6 10.8a15.1 15.1 0 0 0 6.6 6.6l2.2-2.2a1 1 0 0 1 1-.25 11.4 11.4 0 0 0 3.6.57 1 1 0 0 1 1 1V20a1 1 0 0 1-1 1A17 17 0 0 1 3 4a1 1 0 0 1 1-1h3.5a1 1 0 0 1 1 1c0 1.25.2 2.45.57 3.57a1 1 0 0 1-.25 1Z"/></svg>
      630-812-4463
    </li>
    <li>
      <svg viewBox="0 0 24 24"><path d="M7 1h10a2 2 0 0 1 2 2v18a2 2 0 0 1-2 2H7a2 2 0 0 1-2-2V3a2 2 0 0 1 2-2Zm0 3v14h10V4Zm5 15.5a1.2 1.2 0 1 0 0 2.4 1.2 1.2 0 0 0 0-2.4Z"/></svg>
      630-917-3384 EXT. 417
    </li>
    <li>
      <svg viewBox="0 0 24 24"><path d="M2 5h20v14H2Zm2 2v.5l8 5 8-5V7Zm0 2.8V17h16V9.8l-8 5Z"/></svg>
      Tomas@q-rolls-example.com
    </li>
    <li>
      <svg viewBox="0 0 24 24"><path d="M12 2a10 10 0 1 0 0 20 10 10 0 0 0 0-20Zm6.9 6h-3a15.6 15.6 0 0 0-1.4-3.6A8 8 0 0 1 18.9 8ZM12 4a14 14 0 0 1 1.9 4h-3.8A14 14 0 0 1 12 4ZM4.3 14a8 8 0 0 1 0-4h3.4a16 16 0 0 0 0 4Zm.8 2h3a15.6 15.6 0 0 0 1.4 3.6A8 8 0 0 1 5.1 16Zm3-8h-3a8 8 0 0 1 4.4-3.6A15.6 15.6 0 0 0 8.1 8ZM12 20a14 14 0 0 1-1.9-4h3.8A14 14 0 0 1 12 20Zm2.3-6H9.7a14.6 14.6 0 0 1 0-4h4.6a14.6 14.6 0 0 1 0 4Zm.2 5.6a15.6 15.6 0 0 0 1.4-3.6h3a8 8 0 0 1-4.4 3.6Zm1.8-5.6a16 16 0 0 0 0-4h3.4a8 8 0 0 1 0 4Z"/></svg>
      www.Q-rolls-example.com
    </li>
  </ul>
</section>

</body>
</html>
```